KJ Glimmer Cleaning Business Card

We need a business card for our new business, a cleaning company using steam. We already have a logo, and would like a modern-looking card using colors that go well with those in our logo.

```html
<!DOCTYPE html>
<html lang="en">
<head>
<meta charset="utf-8">
<title>KJ Glimmer Cleaning Business Card</title>
<link rel="stylesheet" href="https://fonts.googleapis.com/css2?family=Open+Sans:wght@400;600;700&display=swap">
<style>
  :root {
    --page-bg: #e9e6e1;
    --card-white: #ffffff;
    --brand-blue: #1f6fc4;
    --brand-green: #2f9a3a;
    --text-dark: #3a3a3a;
    --back-deep: #1b3f9e;
    --back-mid: #2c6fd0;
    --back-light: #4a98e6;
    --icon-green: #3aa147;
  }
  * { margin: 0; padding: 0; box-sizing: border-box; }
  html, body { width: 1200px; height: 1024px; overflow: hidden; }
  body {
    background: var(--page-bg);
    font-family: "Open Sans", Arial, sans-serif;
    position: relative;
  }
  .card {
    position: absolute;
    left: 250px;
    width: 700px;
    height: 400px;
    border-radius: 4px;
    overflow: hidden;
    box-shadow: 0 8px 24px rgba(0,0,0,.18);
  }
  .card-front { top: 90px; background: var(--card-white); }
  .card-back {
    top: 534px;
    background: radial-gradient(ellipse at 50% 40%, var(--back-light) 0%, var(--back-mid) 40%, var(--back-deep) 100%);
  }
  .dot-texture {
    position: absolute;
    border-radius: 50%;
  }
  .card-front .dot-texture {
    right: -80px; top: -120px; width: 360px; height: 300px;
    background: radial-gradient(circle, rgba(200,205,212,.45) 0%, rgba(230,232,236,.2) 55%, rgba(255,255,255,0) 75%);
  }
  .card-back .dot-texture {
    left: 60px; bottom: -140px; width: 600px; height: 280px;
    background: radial-gradient(ellipse, rgba(140,190,245,.35) 0%, rgba(80,140,220,.12) 55%, rgba(0,0,0,0) 75%);
  }
  .brand {
    position: absolute;
    display: flex;
    align-items: center;
    gap: 18px;
  }
  .brand-mark {
    width: 78px; height: 78px; border-radius: 50%;
    background: var(--brand-green);
    flex: none;
  }
  .brand-name {
    font-weight: 700;
    color: var(--brand-blue);
    font-size: 34px;
    line-height: 1.1;
  }
  .card-front .brand { left: 48px; top: 60px; }
  .contact-list {
    position: absolute;
    right: 48px; top: 168px;
    list-style: none;
    font-size: 17px;
    color: var(--text-dark);
  }
  .contact-list li { display: flex; align-items: center; gap: 10px; height: 28px; }
  .contact-list svg { width: 16px; height: 16px; flex: none; }
  .person {
    position: absolute;
    left: 48px; bottom: 44px;
  }
  .person-name { color: var(--brand-green); font-size: 21px; font-weight: 400; letter-spacing: .5px; }
  .person-title { color: var(--brand-blue); font-size: 17px; margin-bottom: 8px; }
  .person-address { color: var(--text-dark); font-size: 18px; line-height: 1.35; }
  .card-back .brand {
    left: 50%; top: 50%; transform: translate(-50%, -60%);
    flex-direction: column; gap: 14px;
  }
  .card-back .brand-name { color: #ffffff; font-size: 36px; }
  .back-web {
    position: absolute; left: 0; right: 0; bottom: 30px;
    text-align: center; color: #dfeaff; font-size: 16px; letter-spacing: .3px;
  }
</style>
</head>
<body>
  <section class="card card-front">
    <div class="dot-texture" role="img" aria-label="Faint grey dotted wave decoration"></div>
    <div class="brand">
      <div class="brand-mark"></div>
      <div class="brand-name">KJ Glimmer Cleaning</div>
    </div>
    <ul class="contact-list">
      <li>
        <svg viewBox="0 0 16 16"><path fill="var(--icon-green)" d="M4 1h3l1 4-2 1.5a9 9 0 0 0 3.5 3.5L11 8l4 1v3c0 1-1 2-2 2A12 12 0 0 1 2 3c0-1 1-2 2-2z"/></svg>
        (555) 014-2210
      </li>
      <li>
        <svg viewBox="0 0 16 16"><path fill="var(--icon-green)" d="M4 1h3l1 4-2 1.5a9 9 0 0 0 3.5 3.5L11 8l4 1v3c0 1-1 2-2 2A12 12 0 0 1 2 3c0-1 1-2 2-2z"/></svg>
        (555) 014-2287
      </li>
      <li>
        <svg viewBox="0 0 16 16"><rect x="1" y="3" width="14" height="10" rx="1" fill="var(--icon-green)"/><path d="M1.5 3.5 8 9l6.5-5.5" stroke="#fff" stroke-width="1.3" fill="none"/></svg>
        name@kjglimmercleaning.com
      </li>
      <li>
        <svg viewBox="0 0 16 16"><circle cx="8" cy="8" r="7" fill="var(--icon-green)"/><path d="M1 8h14M8 1c-3 3-3 11 0 14M8 1c3 3 3 11 0 14" stroke="#fff" stroke-width="1" fill="none"/></svg>
        www.kjglimmercleaning.com
      </li>
    </ul>
    <div class="person">
      <p class="person-name">MARCUS HALE</p>
      <p class="person-title">Job Title</p>
      <p class="person-address">42 Willow Bend Lane,<br>Fairview, SC 29000</p>
    </div>
  </section>

  <section class="card card-back">
    <div class="dot-texture" role="img" aria-label="Soft blue dotted wave decoration"></div>
    <div class="brand">
      <div class="brand-mark"></div>
      <div class="brand-name">KJ Glimmer Cleaning</div>
    </div>
    <p class="back-web">www.kjglimmercleaning.com</p>
  </section>
</body>
</html>
```